Van wrap design for 2014 Brask T360 Commercial Van

We are launching a maintenance division for our property company and have bought a new van to advertise our maintenance company. We will be advertising to property owners, the general public etc. our services.
We wish the text to read: Maintenance Division - remodels, plumbing & electrical.

Requirements
Must have
• Both images attached

```html
<!DOCTYPE html>
<html lang="en">
<head>
<meta charset="utf-8">
<title>Hartwell Brothers Properties – Brask T360 Van Wrap</title>
<link rel="stylesheet" href="https://fonts.googleapis.com/css2?family=Oswald:wght@500;600;700&display=swap">
<style>
  :root {
    --page: #ffffff;
    --ink: #111111;
    --wrap-black: #0d0d0d;
    --wrap-white: #f3f3f3;
    --swoosh-grey: #8a8a8a;
    --swoosh-light: #c4c4c4;
    --label-white: #f2f2f2;
    --label-grey: #d6d6d6;
    --text-grey: #7a7a7a;
  }
  * { box-sizing: border-box; margin: 0; padding: 0; }
  html, body {
    width: 1200px; height: 685px; overflow: hidden;
    background: var(--page);
    font-family: "Oswald", sans-serif;
  }
  .wrap-panel {
    position: absolute; left: 86px; top: 150px;
    width: 1028px; height: 310px;
    border-radius: 34px 22px 18px 40px; overflow: hidden;
    background: var(--wrap-white);
  }
  .wrap-background { position: absolute; inset: 0; width: 100%; height: 100%; }

  .brand {
    position: absolute; left: 374px; top: 22px;
    display: flex; align-items: center; gap: 14px;
  }
  .brand-mark {
    width: 52px; height: 52px;
    border: 3px solid var(--ink);
  }
  .brand-name {
    font-weight: 600; font-size: 20px; line-height: 1.08;
    letter-spacing: 2.5px; color: var(--ink); text-transform: uppercase;
  }
  .phone {
    position: absolute; left: 371px; top: 98px;
    font-weight: 600; font-size: 35px; line-height: 1; letter-spacing: 0.5px; color: var(--ink);
  }

  .illustration {
    position: absolute; left: 571px; top: 20px;
    width: 200px; height: 200px; border-radius: 50%;
    border: 3px solid var(--wrap-black);
    background: radial-gradient(circle at 45% 45%, #3f64a8 0%, #8ea2c2 45%, #e2e5ea 100%);
    z-index: 2;
  }
  .team-photo {
    position: absolute; left: 760px; top: 8px;
    width: 268px; height: 302px;
    background:
      linear-gradient(90deg, rgba(243,243,243,0.9) 0%, rgba(243,243,243,0) 14%),
      linear-gradient(180deg, #d8d3cd 0%, #b9a99b 22%, #6c7078 45%, #3b3e44 100%);
    z-index: 1;
  }

  .division {
    position: absolute; left: 224px; top: 200px;
    display: flex; flex-direction: column; align-items: flex-end; gap: 3px;
  }
  .division-label {
    font-weight: 700; font-size: 34px; line-height: 1;
    padding: 3px 7px 4px; border-radius: 6px; text-transform: uppercase;
  }
  .division-label--primary { background: var(--label-white); color: var(--ink); }
  .division-label--secondary { background: var(--label-grey); color: var(--text-grey); }

  .divider {
    position: absolute; left: 446px; top: 200px;
    width: 4px; height: 86px; background: var(--label-white);
  }
  .services {
    position: absolute; left: 458px; top: 202px;
    list-style: none; display: flex; flex-direction: column; gap: 3px;
  }
  .service {
    font-weight: 700; font-size: 20px; line-height: 1;
    padding: 2px 5px 3px; border-radius: 5px; text-transform: uppercase; width: fit-content;
  }
  .service--remodels { background: var(--label-white); color: var(--ink); }
  .service--plumbing { background: var(--label-grey); color: var(--text-grey); }
  .service--electrical { background: var(--label-white); color: var(--ink); }
</style>
</head>
<body>
  <main class="wrap-panel">
    <svg class="wrap-background" viewBox="0 0 1028 310" preserveAspectRatio="none" aria-hidden="true">
      <path d="M0 125 C 150 150, 300 188, 480 190 S 850 140, 1028 115 L1028 310 L0 310 Z" fill="var(--wrap-black)"/>
      <path d="M0 112 C 150 138, 300 176, 480 178 S 850 108, 1028 82 L1028 104 C 850 128, 650 186, 480 188 S 150 148, 0 124 Z" fill="var(--swoosh-grey)"/>
      <path d="M0 104 C 150 128, 300 166, 480 168 S 850 96, 1028 70 L1028 78 C 850 104, 650 174, 480 175 S 150 134, 0 110 Z" fill="var(--swoosh-light)"/>
    </svg>

    <div class="brand">
      <span class="brand-mark" aria-hidden="true"></span>
      <p class="brand-name">Hartwell<br>Brothers<br>Properties</p>
    </div>
    <p class="phone">0198 765 432</p>

    <div class="illustration" role="img" aria-label="Illustration of a building under construction with a tower crane over blueprints"></div>
    <div class="team-photo" role="img" aria-label="Photo of the two brothers who run the company, in suits"></div>

    <div class="division">
      <span class="division-label division-label--primary">Maintenance</span>
      <span class="division-label division-label--secondary">Division</span>
    </div>
    <span class="divider" aria-hidden="true"></span>
    <ul class="services">
      <li class="service service--remodels">Remodels</li>
      <li class="service service--plumbing">Plumbing</li>
      <li class="service service--electrical">Electrical.</li>
    </ul>
  </main>
</body>
</html>
```